Texas Recycling and dump company needs Flyer design

We need a flyer design for a new company based in Austin Texas called 'Salvage Grove'. We receive dump materials on our property along with sell repurposed materials. We would like our design to include our logo along with add some creative designs to the flyer. Please use the attached image file as an outline. Blank boxes can be used for additional images.

Target Market(s)

Handing out flyers to new companies and hopefully getting contracts with them.

Font styles to use
Serif
Sans Serif

Requirements
Must have
• double sided
• images
Nice to have
• QR code with our website

```html
<!DOCTYPE html>
<html lang="en">
<head>
<meta charset="utf-8">
<title>Salvage Grove — Flyer, Front and Back</title>
<link href="https://fonts.googleapis.com/css2?family=Arimo:wght@400;700&family=Oswald:wght@500;600&display=swap" rel="stylesheet">
<style>
  :root{
    --green:#8dc63f;
    --blue:#1b6fb9;
    --ink-blue:#1d6bb5;
    --white:#ffffff;
    --bg-light:#cfcdcd;
    --bg-dark:#a7a6a6;
  }
  *{box-sizing:border-box;margin:0;padding:0}
  html,body{width:1200px;height:1200px;overflow:hidden}
  body{
    background:radial-gradient(ellipse at 50% 30%,var(--bg-light),var(--bg-dark));
    font-family:"Arimo",Arial,sans-serif;
    position:relative;
  }
  .stage{
    position:absolute;left:42px;top:216px;
    width:1015px;height:697px;
    transform:scale(1.1);transform-origin:0 0;
  }
  .flyer{
    position:absolute;background:var(--white);overflow:hidden;
    box-shadow:0 18px 22px -10px rgba(0,0,0,.35);
  }
  .flyer--front{left:0;top:2px;width:489px;height:693px}
  .flyer--back{left:523px;top:0;width:492px;height:697px}

  .band{position:absolute;left:0;width:100%}
  .band--green{background:var(--green)}
  .band--blue{background:var(--blue)}

  .tile{
    position:absolute;width:117px;height:117px;background:var(--white);
    border:2px solid var(--green);
    display:flex;align-items:center;justify-content:center;text-align:center;
    padding-bottom:16px;
    color:var(--ink-blue);font-weight:700;font-size:15.5px;line-height:1.15;
    box-shadow:0 9px 6px -5px rgba(0,0,0,.35);
  }
  .tile--plain{border-color:transparent}

  .brand{position:absolute;left:0;width:100%;text-align:center}
  .brand__mark{
    width:56px;height:56px;border-radius:50%;background:var(--white);
    margin:0 auto 14px;
  }
  .brand__name{color:var(--white);font-size:22px;font-weight:400;letter-spacing:1px}

  .slogan{color:var(--white);text-align:center}
  .slogan__main{font-size:26px;font-weight:700;margin-top:28px}
  .slogan__sub{font-size:21px;margin-top:8px}
  .slogan__addr{font-size:18px;font-weight:700;margin-top:8px}

  .contact{position:absolute;left:0;width:100%;color:var(--ink-blue)}
  .contact__row{display:flex;align-items:center;justify-content:center;gap:10px}
  .contact__phone{font-family:"Oswald",sans-serif;font-weight:600;font-size:39px;line-height:1}
  .contact__web{font-size:26px;line-height:1}

  .headline{position:absolute;left:0;top:30px;width:100%;text-align:center;color:var(--white)}
  .headline__title{font-family:"Oswald",sans-serif;font-weight:600;font-size:36px;line-height:1;transform:scaleX(.9)}
  .headline__sub{font-weight:700;font-size:30px;margin-top:6px}
</style>
</head>
<body>
<div class="stage">

  <section class="flyer flyer--front">
    <div class="band band--green" style="top:0;height:155px"></div>
    <div class="brand" style="top:24px">
      <div class="brand__mark"></div>
      <div class="brand__name">SALVAGE GROVE</div>
    </div>

    <div class="tile" style="left:40px;top:139px">CONCRETE</div>
    <div class="tile" style="left:186px;top:139px">ASPHALT</div>
    <div class="tile" style="left:331px;top:139px">CLEAN FILL</div>
    <div class="tile" style="left:108px;top:280px">WOOD<br>BRUSH</div>
    <div class="tile" style="left:253px;top:280px">C&amp;D</div>

    <div class="band band--blue slogan" style="top:435px;height:147px">
      <div class="slogan__main">CLEANER THE PRODUCT</div>
      <div class="slogan__sub">LOWER THE PRICE</div>
      <div class="slogan__addr">2810 CEDAR MILL RD AUSTIN</div>
    </div>

    <div class="contact" style="top:604px">
      <div class="contact__row">
        <svg width="30" height="30" viewBox="0 0 30 30" aria-hidden="true">
          <rect width="30" height="30" rx="6" fill="var(--green)"/>
          <path d="M10 6c1.5 0 3 3 3 4.5S11 12 11 13s3.5 5 5 5 2-2 3-2 4 1.5 4 3-2 4-5 4C11 23 6 17 6 11c0-3 2.5-5 4-5z" fill="#fff"/>
        </svg>
        <span class="contact__phone">512-555-0148</span>
      </div>
      <div class="contact__row" style="margin-top:6px">
        <svg width="20" height="20" viewBox="0 0 20 20" aria-hidden="true" fill="none" stroke="var(--green)" stroke-width="1.6">
          <circle cx="10" cy="10" r="8"/><ellipse cx="10" cy="10" rx="3.5" ry="8"/><path d="M2 10h16M3.5 6h13M3.5 14h13"/>
        </svg>
        <span class="contact__web">salvagegroveatx.com</span>
      </div>
    </div>
  </section>

  <section class="flyer flyer--back">
    <div class="band band--blue" style="top:0;height:157px"></div>
    <div class="band band--green" style="top:599px;height:98px"></div>
    <div class="headline">
      <div class="headline__title">LANDSCAPE MATRIALS</div>
      <div class="headline__sub">HOT DEALS</div>
    </div>

    <div class="tile" style="left:39px;top:138px">MULCH</div>
    <div class="tile" style="left:186px;top:138px">HOT<br>DEALS?</div>
    <div class="tile" style="left:333px;top:138px">TOP SOIL</div>

    <div class="tile" style="left:39px;top:281px">DEC<br>GRA</div>
    <div class="tile" style="left:186px;top:281px"></div>
    <div class="tile" style="left:333px;top:281px">BASE</div>

    <div class="tile" style="left:39px;top:424px">ROCK</div>
    <div class="tile" style="left:186px;top:424px"></div>
    <div class="tile" style="left:333px;top:424px">ASPHALT</div>

    <div class="tile tile--plain" style="left:39px;top:564px"></div>
    <div class="tile tile--plain" style="left:186px;top:564px"></div>
    <div class="tile tile--plain" style="left:333px;top:564px"></div>
  </section>

</div>
</body>
</html>
```